Flyer for an online formula one racing league

Hello.

I am looking for the perfect one page facebook/instagram style flyer for an online formula one racing league. The racing league is called 'VOLKA RACING LEAGUE'.

Information that MUST be on the new flyer is already on the old flyer I have uploaded here. In addition to including: The Volka racing league 'R' logo I have uploaded AND the text: 'Very popular, clean and competitive racing league, running for its 4th season. Why not join with a friend? Race times, Mondays, Tuesdays and Wednesdays each at 8pm UK TIME Message below for any questions. (Spacing of information is not important, however all the information in regards to the racing I have just mentioned MUST BE on the flyer, this includes info from old pic, logo and the other info I just mentioned).

It would be beneficial to have lots of dark blue on the flyer and the new flyer to be a lot different to the original flyer I uploaded, but this is not essential.

I apologise if I did not explain very well, any questions, please message me.

The best flyer should look the most attractive to someone that might be interested in joining an online formula one racing league.

I used this website before to create the perfect logo for my Sunday League team last year, and I was very impressed. I look forward to seeing your submissions.

Target Market(s)

No specific target, more something that may attract someone into joining a formula one online racing league

Industry/Entity Type

e sports/formula one

Colors
0054AA
0677BA
7BADD7
CADEEF
E8F1F8

Requirements
Must have
• Read product description please
Should not have
• Ignoring product description!

```html
<!DOCTYPE html>
<html lang="en">
<head>
<meta charset="utf-8">
<title>Volka Racing League – New Season</title>
<link href="https://fonts.googleapis.com/css2?family=Noto+Serif:wght@700&family=Poppins:ital,wght@0,300;0,500;0,600;0,700;0,800;1,500&display=swap" rel="stylesheet">
<style>
  :root {
    --navy: #0e1f6f;
    --navy-deep: #0a1440;
    --gold: #fbb812;
    --white: #ffffff;
  }
  * { margin: 0; padding: 0; box-sizing: border-box; }
  html, body {
    width: 1200px;
    height: 1200px;
    overflow: hidden;
    background: var(--navy);
  }
  .flyer {
    position: relative;
    width: 1200px;
    height: 1200px;
    background: var(--navy);
    font-family: "Poppins", sans-serif;
    color: var(--white);
  }
  .centered {
    position: absolute;
    left: 0;
    width: 100%;
    text-align: center;
    white-space: nowrap;
  }
  .league-title {
    top: 48px;
    font-family: "Noto Serif", serif;
    font-weight: 700;
    font-size: 78px;
    letter-spacing: 1px;
    line-height: 1;
  }
  .tag-row {
    position: absolute;
    top: 172px;
    left: 0;
    width: 100%;
    display: flex;
    justify-content: center;
    gap: 27px;
  }
  .tag {
    background: var(--gold);
    color: var(--navy);
    font-weight: 700;
    font-size: 40px;
    line-height: 63px;
    height: 63px;
    padding: 0 14px;
    letter-spacing: 0.5px;
  }
  .subtitle {
    top: 250px;
    font-weight: 800;
    font-size: 51px;
    letter-spacing: 2px;
    line-height: 1;
  }
  .season-news {
    top: 322px;
    font-weight: 500;
    font-size: 42px;
    line-height: 1;
  }
  .season-count {
    top: 400px;
    font-style: italic;
    font-weight: 500;
    font-size: 40px;
    color: var(--gold);
    line-height: 1;
  }
  .brand-mark {
    position: absolute;
    left: 444px;
    top: 467px;
    width: 322px;
    height: 322px;
    border-radius: 50%;
    background: var(--navy-deep);
    display: flex;
    align-items: center;
    justify-content: center;
    font-weight: 800;
    font-size: 64px;
    letter-spacing: 2px;
    color: var(--white);
  }
  .invite {
    top: 815px;
    font-weight: 800;
    font-size: 45px;
    color: var(--gold);
    line-height: 1;
  }
  .invite .qmark { font-size: 62px; vertical-align: -4px; }
  .days-box {
    position: absolute;
    left: 180px;
    top: 880px;
    width: 851px;
    height: 98px;
    background: var(--white);
    color: var(--navy);
    transform: rotate(-0.5deg);
    display: flex;
    align-items: center;
    justify-content: center;
    font-weight: 600;
    font-size: 36px;
  }
  .days-box strong, .time-box strong { font-weight: 800; }
  .time-box {
    position: absolute;
    left: 369px;
    top: 975px;
    width: 467px;
    height: 86px;
    background: var(--gold);
    color: var(--navy);
    transform: rotate(0.4deg);
    display: flex;
    align-items: center;
    justify-content: center;
    font-weight: 700;
    font-size: 38px;
  }
  .time-box .zone { font-size: 26px; margin-left: 8px; }
  .contact-note {
    top: 1080px;
    font-weight: 300;
    font-size: 32px;
    color: var(--gold);
    line-height: 1;
  }
  .growth-note {
    top: 1138px;
    font-weight: 500;
    font-size: 31px;
    letter-spacing: 0.5px;
    line-height: 1;
  }
</style>
</head>
<body>
  <main class="flyer">
    <h1 class="centered league-title">VOLKA RACING LEAGUE</h1>

    <div class="tag-row">
      <span class="tag">POPULAR</span>
      <span class="tag">CLEAN</span>
      <span class="tag">COMPETITIVE</span>
    </div>

    <h2 class="centered subtitle">RACING LEAGUE</h2>
    <p class="centered season-news">NEW SEASON JUST STARTING!!!</p>
    <p class="centered season-count">Running For Its 4th Season</p>

    <div class="brand-mark">VOLKA</div>

    <p class="centered invite">WHY NOT JOIN WITH A FRIEND<span class="qmark">?</span></p>

    <div class="days-box"><span><strong>Days:</strong> Monday, Tuesday and Wednesday</span></div>
    <div class="time-box"><span><strong>Timings: 8pm</strong><span class="zone">(UK Time)</span></span></div>

    <p class="centered contact-note">Message us for any query</p>
    <p class="centered growth-note">3 DIVISIONS CURRENTLY AND LOOKING TO KEEP GROWING!</p>
  </main>
</body>
</html>
```